Need Letterhead Design & Matching Business Card

I have a logo that I love already. But the letterhead is less than appealing and boring. I'd like a design for my letterhead which I will match with business cards. Also, I'd like to have used fonts that are generally available, as my current letterhead uses a font named "SPACE" which nobody has unless they download it...so when a Word version is forwarded, it looks awful on the receiver's screed due to not having the font. That being said, modern is the look we like and are going for.

My business is "Halloran Brightmoor PC" - a law firm specializing in representing people who have suffered catastrophic injuries or death (plane, auto, train crashes etc.).

See attached letterhead, which has all of the pertinent information. My logo is also attached in various formats.

```html
<!DOCTYPE html>
<html lang="en">
<head>
<meta charset="utf-8">
<title>Halloran Brightmoor PC – Stationery</title>
<link rel="stylesheet" href="https://fonts.googleapis.com/css2?family=Inter:wght@300;400&display=swap">
<style>
  :root {
    --backdrop: #4a4a4a;
    --paper: #ebebeb;
    --paper-light: #f1f1f1;
    --ink: #2b2b2b;
    --ink-soft: #4a4a4a;
    --mark-dark: #262626;
    --watermark: #dcdcdc;
  }
  * { margin: 0; padding: 0; box-sizing: border-box; }
  html, body {
    width: 1200px; height: 800px; overflow: hidden;
    background: var(--backdrop);
    font-family: "Inter", Arial, sans-serif;
    color: var(--ink);
  }
  .stationery { position: relative; width: 1200px; height: 800px; }

  .sheet {
    position: absolute;
    background: linear-gradient(160deg, var(--paper) 0%, var(--paper-light) 100%);
  }
  .letterhead { left: 458px; top: 162px; width: 340px; height: 478px; }
  .card { width: 201px; height: 115px; }
  .card-front { left: 362px; top: 216px; }
  .card-back { left: 362px; top: 347px; }

  .brand { position: absolute; display: flex; align-items: center; }
  .brand-square { background: var(--mark-dark); flex: none; }
  .brand-name {
    font-weight: 300; text-transform: uppercase; color: var(--ink);
    line-height: 1.15; letter-spacing: 0.02em;
  }
  .letterhead .brand { left: 117px; top: 22px; gap: 6px; }
  .letterhead .brand-square { width: 27px; height: 27px; }
  .letterhead .brand-name { font-size: 11.5px; }

  .card-front .brand { left: 19px; top: 21px; gap: 4px; }
  .card-front .brand-square { width: 18px; height: 18px; }
  .card-front .brand-name { font-size: 7.5px; }

  .card-back .brand-square {
    position: absolute; left: 86px; top: 42px; width: 32px; height: 32px;
  }

  .watermark {
    position: absolute; left: 135px; top: 205px; width: 70px; height: 68px;
    border: 3px solid var(--watermark);
  }

  .contact { position: absolute; text-transform: uppercase; color: var(--ink-soft); font-weight: 400; }
  .letterhead .contact { top: 424px; font-size: 4.8px; line-height: 10.6px; }
  .letterhead .contact-web { left: 34px; }
  .letterhead .contact-office { left: 228px; }
  .card .contact { top: 80px; font-size: 4px; line-height: 5.6px; }
  .card .contact-web { left: 25px; }
  .card .contact-office { left: 108px; }
</style>
</head>
<body>
<main class="stationery">

  <section class="sheet letterhead">
    <div class="brand">
      <span class="brand-square"></span>
      <span class="brand-name">Halloran<br>Brightmoor PC</span>
    </div>
    <span class="watermark"></span>
    <address class="contact contact-web">
      rowan@halloranbrightmoor.com<br>
      www.halloranbrightmoor.com<br>
      Tel: (855) 555-0147
    </address>
    <address class="contact contact-office">
      D. Rowan Mercer, Esq. | President<br>
      4120 Larkspur Ave. | Suite 800<br>
      Westbrook Hills, CA 90300
    </address>
  </section>

  <section class="sheet card card-front">
    <div class="brand">
      <span class="brand-square"></span>
      <span class="brand-name">Halloran<br>Brightmoor PC</span>
    </div>
    <address class="contact contact-web">
      rowan@halloranbrightmoor.com<br>
      www.halloranbrightmoor.com<br>
      Tel: (855) 555-0147
    </address>
    <address class="contact contact-office">
      D. Rowan Mercer, Esq. | President<br>
      4120 Larkspur Ave. | Suite 800<br>
      Westbrook Hills, CA 90300
    </address>
  </section>

  <section class="sheet card card-back">
    <span class="brand-square"></span>
  </section>

</main>
</body>
</html>
```